Mine Engineering Consultancy specializing in
* Pit optimization
* Mine Design
* Scheduling
* Mine Rehabilitation

Industry/Entity Type

Mining

Contact Information for Business Card

RVT Mining Pty Ltd
Derek Holloway
Director/Principle Mining Engineer
Mobile 0413582961
Email derek.holloway@rvtmining-example.com

```html
<!DOCTYPE html>
<html lang="en">
<head>
<meta charset="utf-8">
<title>RVT Mining Pty Ltd – Business Card</title>
<link href="https://fonts.googleapis.com/css2?family=Roboto:wght@300;400;700&display=swap" rel="stylesheet">
<style>
  :root {
    --page-bg: #e9e9e9;
    --brand-blue: #1565ad;
    --slate: #6b6c6e;
    --silver: #b3b4b6;
    --white: #ffffff;
    --soft-blue: #a9c4e2;
    --surname-grey: #c7c9cc;
  }
  * { margin: 0; padding: 0; box-sizing: border-box; }
  html, body { width: 1200px; height: 720px; overflow: hidden; }
  body {
    background: var(--page-bg);
    font-family: "Roboto", Arial, sans-serif;
    display: flex;
    align-items: center;
    justify-content: center;
    gap: 40px;
  }
  .card {
    position: relative;
    width: 520px;
    height: 297px;
    overflow: hidden;
    box-shadow: 0 6px 18px rgba(0,0,0,0.18);
  }
  .card-shapes { position: absolute; inset: 0; }
  .shape-blue { fill: var(--brand-blue); }
  .shape-slate { fill: var(--slate); }
  .shape-silver { fill: var(--silver); }

  /* Front */
  .contact {
    position: absolute;
    left: 232px;
    top: 118px;
    transform: rotate(-24deg);
    transform-origin: left top;
    color: var(--soft-blue);
  }
  .contact-name {
    font-weight: 700;
    font-size: 21px;
    color: var(--white);
    letter-spacing: 0.3px;
  }
  .contact-name .surname { color: var(--surname-grey); }
  .contact-title {
    font-size: 11.5px;
    color: var(--white);
    margin-top: 2px;
  }
  .contact-details {
    font-weight: 300;
    font-size: 11.5px;
    line-height: 1.35;
    margin-top: 14px;
    margin-left: 20px;
  }
  .front-company {
    position: absolute;
    left: 40px;
    bottom: 34px;
    display: flex;
    align-items: center;
    gap: 10px;
    font-weight: 700;
    font-size: 20px;
    color: var(--brand-blue);
  }
  .brand-square {
    width: 16px; height: 16px;
    background: var(--brand-blue);
  }

  /* Back */
  .back-company {
    position: absolute;
    left: 34px;
    top: 112px;
    width: 230px;
    font-weight: 700;
    font-size: 30px;
    line-height: 1.15;
    color: var(--white);
  }
  .services {
    position: absolute;
    left: 268px;
    top: 22px;
    list-style: none;
    color: var(--white);
    font-size: 13.5px;
    line-height: 1.55;
  }
  .services li::before { content: "• "; }
  .services li:nth-child(2) { margin-left: 18px; }
  .services li:nth-child(3) { margin-left: 36px; }
  .services li:nth-child(4) { margin-left: 54px; }
</style>
</head>
<body>

  <section class="card card-front" aria-label="Business card front">
    <svg class="card-shapes" viewBox="0 0 520 297" preserveAspectRatio="none">
      <rect class="shape-silver" width="520" height="297"/>
      <polygon class="shape-slate" points="60,0 236,0 205,120"/>
      <polygon class="shape-blue" points="236,0 520,0 520,297 330,297 205,120"/>
    </svg>
    <div class="contact">
      <p class="contact-name">DEREK <span class="surname">HOLLOWAY</span></p>
      <p class="contact-title">Director/Principle Mining Engineer</p>
      <p class="contact-details">0413582961<br>derek.holloway@rvtmining-example.com</p>
    </div>
    <div class="front-company">
      <span class="brand-square"></span>
      <span>RVT Mining Pty Ltd</span>
    </div>
  </section>

  <section class="card card-back" aria-label="Business card back">
    <svg class="card-shapes" viewBox="0 0 520 297" preserveAspectRatio="none">
      <rect class="shape-blue" width="520" height="297"/>
      <polygon class="shape-slate" points="205,0 520,0 520,80 390,210"/>
      <polygon class="shape-silver" points="520,80 520,297 330,297 390,210"/>
    </svg>
    <p class="back-company">RVT Mining Pty Ltd</p>
    <ul class="services">
      <li>Pit Optimization</li>
      <li>Mine Design</li>
      <li>Scheduling</li>
      <li>Mine Rehabilitation</li>
    </ul>
  </section>

</body>
</html>
```